NEW Wordpress Website Design for a Dynamic Long Term Healthcare Company in Hawaii

I would like a new website design for my current company, Marlow Haven Partners, which has two different brands - Marlow Homecare and Marlow Senior Living. You can see the current website at www.marlowhaven.example. The website should be built using Wordpress Software and the Elementor theme. The website should have a local Hawaii island/tropical feel, but look professional for healthcare. I'm looking for something fresh, and want the designer to select colors, styles, etc.

In the Header, on all pages, I would like a menu that includes Home Care, Senior Living, Rates, and About Us.
Under each of the Header Menu Titles, I would like these drop downs included:
Home Care (drop down pages)- Nurse Aide Care, 24-Hour Home Care, Skilled Nursing, Lifestyle Aide, Hospice at Home, Bathing & Meal Service.
Senior Living (drop down pages) - Long-Term Stay, Short-Term Stay.
Rates (drop down page) - Rates.
About Us (drop down pages) - Our Mission, Ohana Talk, About Doreen Marlow.

In the footer, on all pages, you should include the address: 248 Lanakila Ave, Suite 310, Honolulu, HI 96817. Phone number: 808-555-0173
The footer should also include buttons for a page called Learn, Caregiver Jobs, and each of the service page links to include: Nurse Aide Care, 24-Hour Home Care, Skilled Nursing, Lifestyle Aide, Hospice at Home, Bathing & Meal Service.
Please don't take the current website and redesign a few aspects. I'm looking for a completely different look and feel.

Target Market(s)

40-80 year olds

Industry/Entity Type

Long Term Healthcare

Coding

Coded - Design and coding required

Requirements
Should not have
• Our existing website as a template. We are looking for a complete redesign. Thank you.

```html
<!DOCTYPE html>
<html lang="en">
<head>
<meta charset="utf-8">
<title>Marlow Haven Partners</title>
<link href="https://fonts.googleapis.com/css2?family=Poppins:wght@400;500;600&family=Merriweather:wght@400;700&display=swap" rel="stylesheet">
<style>
:root{
  --teal:#174a4a;
  --teal-dark:#123d3d;
  --white:#ffffff;
  --ink:#3a3a3a;
  --muted:#6b6b6b;
  --panel:#f3f3f3;
  --field:#ffffff;
  --star:#e9a23b;
  --quote:#dde4e4;
}
*{box-sizing:border-box;margin:0;padding:0}
html,body{width:1200px;height:2826px;overflow:hidden}
body{position:relative;background:var(--white);font-family:'Poppins',sans-serif;color:var(--ink)}
.abs{position:absolute}

.topbar{left:0;top:0;width:1200px;height:39px;background:var(--teal);color:var(--white);font-size:13px}
.topbar .item{position:absolute;top:11px;display:flex;align-items:center;gap:10px}
.topbar .social{position:absolute;top:12px;display:flex;gap:10px;right:88px}
.topbar .social span{width:14px;height:14px;border-radius:50%;background:var(--white);display:block}

.header{left:0;top:39px;width:1200px;height:70px;background:var(--white)}
.brand{position:absolute;left:89px;top:18px;display:flex;align-items:center;gap:10px;font-family:'Merriweather',serif;font-size:21px;color:var(--teal)}
.brand .mark{width:34px;height:34px;border-radius:6px;background:var(--teal)}
.nav{position:absolute;left:611px;top:26px;display:flex;gap:16px;font-size:13px;color:#444}
.nav span::after{content:"";display:inline-block;width:5px;height:5px;border-right:1.5px solid #444;border-bottom:1.5px solid #444;transform:rotate(45deg);margin-left:9px;position:relative;top:-3px}
.btn{background:var(--teal);color:var(--white);border-radius:30px;display:flex;align-items:center;justify-content:center;font-weight:500}
.header .btn{position:absolute;left:988px;top:17px;width:122px;height:37px;font-size:14px}

.hero{left:0;top:109px;width:1200px;height:586px;background:linear-gradient(180deg,#8a7a3e 0%,#a99a4a 30%,#6c5d34 65%,#2a2316 88%,#000 100%)}
.hero h1{position:absolute;left:0;width:1200px;top:395px;text-align:center;color:var(--white);font-family:'Merriweather',serif;font-weight:700;font-size:33px;line-height:40px}
.hero .pill{position:absolute;left:527px;top:486px;width:146px;height:36px;border-radius:20px;background:#f3f1ec;color:#333;font-size:14px;display:flex;align-items:center;justify-content:center}

.consult{left:123px;top:653px;width:955px;height:557px;background:var(--panel);border-radius:20px;box-shadow:0 10px 40px rgba(0,0,0,.06)}
.consult h2{position:absolute;left:0;width:955px;top:36px;text-align:center;font-family:'Merriweather',serif;font-weight:400;font-size:24px;line-height:36px;color:#3e3e3e}
.field{position:absolute;background:var(--field);border-radius:8px;font-size:12.5px;color:#555;padding-left:26px;display:flex;align-items:center;box-shadow:0 2px 6px rgba(0,0,0,.04)}
.field.area{align-items:flex-start;padding-top:16px}
.consult .btn{position:absolute;left:403px;top:472px;width:147px;height:50px;font-size:17px;font-weight:600}

.quote-band{left:0;top:1300px;width:1200px;height:148px;background:var(--teal);color:var(--white);text-align:center;font-family:'Merriweather',serif;font-weight:700;font-variant:small-caps;font-size:28px;line-height:40px;padding-top:30px}

.photo{border-radius:10px}
.card-title{text-align:center;font-family:'Merriweather',serif;font-size:18px;color:#333;width:500px}
.card-text{text-align:center;font-size:12.5px;line-height:20px;color:var(--muted);width:440px}
.cards .btn{height:40px;font-size:14px}

.testimonials h2{left:0;width:1200px;top:2175px;text-align:center;font-family:'Merriweather',serif;font-weight:400;font-size:24px;color:#333}
.quote-mark{z-index:0}
.t-text{left:310px;width:580px;top:2273px;text-align:center;font-size:14.5px;line-height:21px;color:#444;z-index:1}
.t-name{left:0;width:1200px;top:2343px;text-align:center;font-family:'Merriweather',serif;font-size:16px;color:#333}
.dot{width:11px;height:11px;border-radius:50%;background:#ccc}

.footer{left:0;top:2467px;width:1200px;height:359px;background:var(--teal);color:var(--white)}
.footer h3{position:absolute;font-family:'Merriweather',serif;font-weight:700;font-size:19px}
.footer .links{position:absolute;left:371px;top:88px;font-size:12.5px;line-height:20px;list-style:none}
.footer .divider{position:absolute;width:1px;background:rgba(255,255,255,.35)}
.footer .ci{position:absolute;left:582px;font-size:13px;line-height:18px}
.footer .ci b{font-family:'Merriweather',serif;font-size:13px}
.footer .ci .row{display:flex;gap:6px}
.footer .soc{position:absolute;top:95px;width:40px;height:40px;border-radius:50%;background:rgba(255,255,255,.14)}
.footer .badge{position:absolute;top:158px;width:80px;height:80px;border-radius:50%;background:#f6ecea;border:3px solid #e6d8d5}
.footer .flogo{position:absolute;left:140px;top:100px;width:180px;text-align:center;font-family:'Merriweather',serif;font-size:22px;line-height:28px}
.footer .flogo .mark{width:44px;height:44px;border-radius:8px;background:var(--white);margin:0 auto 14px}
.footer .rule{position:absolute;left:89px;top:300px;width:1022px;height:1px;background:rgba(255,255,255,.3)}
.footer .copy{position:absolute;left:0;width:1200px;top:322px;text-align:center;font-family:'Merriweather',serif;font-weight:700;font-variant:small-caps;font-size:12px}
.chat{position:absolute;left:1128px;top:283px;width:40px;height:34px;border-radius:50%;background:var(--white)}
</style>
</head>
<body>

<div class="abs topbar">
  <div class="item" style="left:89px">
    <svg width="13" height="13" viewBox="0 0 24 24"><path fill="#fff" d="M6.6 10.8a15 15 0 0 0 6.6 6.6l2.2-2.2c.3-.3.7-.4 1-.2 1.1.4 2.3.6 3.6.6.6 0 1 .4 1 1V20c0 .6-.4 1-1 1A17 17 0 0 1 3 4c0-.6.4-1 1-1h3.5c.6 0 1 .4 1 1 0 1.2.2 2.4.6 3.6.1.3 0 .7-.2 1z"/></svg>
    (808) 555-0173</div>
  <div class="item" style="left:279px">
    <svg width="15" height="12" viewBox="0 0 24 18"><rect width="24" height="18" rx="2" fill="#fff"/><path d="M1 2l11 8 11-8" stroke="#174a4a" stroke-width="2" fill="none"/></svg>
    info@marlowhaven.example</div>
  <div class="item" style="left:510px">
    <svg width="11" height="15" viewBox="0 0 16 22"><path fill="#fff" d="M8 0a8 8 0 0 0-8 8c0 6 8 14 8 14s8-8 8-14a8 8 0 0 0-8-8zm0 11a3 3 0 1 1 0-6 3 3 0 0 1 0 6z"/></svg>
    1450 Kalakaua Ave #820, Honolulu, HI 96826</div>
  <div class="social"><span></span><span></span><span></span></div>
</div>

<div class="abs header">
  <div class="brand"><span class="mark"></span>Marlow Haven Partners</div>
  <div class="nav"><span>Home Care</span><span>Senior Living</span><span>Rates</span><span>About Us</span></div>
  <div class="btn">Contact Us</div>
</div>

<div class="abs hero" role="img" aria-label="Caregiver leading three seniors in a light dumbbell exercise in a sunny living room">
  <h1>HAWAII'S CHOICE HOMECARE &amp;<br>SENIOR LIVING</h1>
  <div class="pill">Info &amp; Rates</div>
</div>

<div class="abs consult">
  <h2>SCHEDULE A COMPLIMENTARY CARE<br>CONSULTATION</h2>
  <div class="field" style="left:56px;top:122px;width:273px;height:54px">Name*</div>
  <div class="field" style="left:341px;top:122px;width:273px;height:54px">Email*</div>
  <div class="field" style="left:624px;top:122px;width:273px;height:54px">Phone*</div>
  <div class="field" style="left:56px;top:191px;width:841px;height:54px">How Can We Help?</div>
  <div class="field" style="left:56px;top:261px;width:414px;height:54px">Questions/comments</div>
  <div class="field" style="left:483px;top:261px;width:414px;height:54px">How did you hear about us?</div>
  <div class="field area" style="left:56px;top:330px;width:841px;height:127px">May We Email You About This?</div>
  <div class="btn">Submit</div>
</div>

<div class="abs quote-band">"Caregiving is a series of small acts of care that<br>alter the course of someone's life."</div>

<div class="cards">
  <div class="abs photo" style="left:89px;top:1537px;width:500px;height:374px;background:linear-gradient(160deg,#d9cf7a,#b9a866 45%,#6e8aa6 80%,#ddd6c4)" role="img" aria-label="Homecare aide helping a senior man sit up on his bed"></div>
  <div class="abs photo" style="left:610px;top:1537px;width:501px;height:374px;background:linear-gradient(160deg,#cfc58a,#a48a5c 45%,#4e6fa8 75%,#7a5a3e)" role="img" aria-label="Caregiver and resident sharing a photo album on a living room sofa"></div>
  <div class="abs card-title" style="left:89px;top:1930px">PROFESSIONAL CARE IN YOUR HOME</div>
  <div class="abs card-title" style="left:610px;top:1930px">TRUSTED CARE IN OUR HOME</div>
  <div class="abs card-text" style="left:119px;top:1958px">Marlow Homecare understands that every person's care journey is unique. We tailor our in-home services to meet the diverse nurturing experience of professional quality care and safety within the comfort and convenience of your own home.</div>
  <div class="abs card-text" style="left:640px;top:1958px">Marlow Senior Living creates a warm, supportive, and enriching care home environment where seniors can thrive in their golden years. We provide residential care that promotes well-being, connection, and dignity of each individual.</div>
  <div class="abs btn" style="left:212px;top:2049px;width:262px">schedule care assessment</div>
  <div class="abs btn" style="left:780px;top:2049px;width:164px">schedule Tour</div>
</div>

<div class="testimonials">
  <h2 class="abs">TESTIMONIALS</h2>
  <svg class="abs quote-mark" style="left:538px;top:2215px" width="124" height="72" viewBox="0 0 124 72">
    <path fill="#dde4e4" d="M0 72V40C0 14 14 2 40 0v14c-12 2-18 10-18 22h18v36zM64 72V40C64 14 78 2 104 0v14c-12 2-18 10-18 22h18v36z"/>
  </svg>
  <div class="abs t-text">At Marlow Haven Partners, our mission is to provide compassionate and professional long-term healthcare services that empower individuals to maintain their highest level</div>
  <div class="abs t-name">Leilani K.</div>
  <svg class="abs" style="left:563px;top:2367px" width="74" height="14" viewBox="0 0 74 14">
    <g fill="#e9a23b">
      <path id="s" d="M7 0l2 4.6 5 .4-3.8 3.3 1.2 5L7 10.6 2.6 13.3l1.2-5L0 5l5-.4z"/>
      <use href="#s" x="15"/><use href="#s" x="30"/><use href="#s" x="45"/><use href="#s" x="60"/>
    </g>
  </svg>
  <div class="abs dot" style="left:1099px;top:2257px;background:var(--teal)"></div>
  <div class="abs dot" style="left:1099px;top:2275px"></div>
  <div class="abs dot" style="left:1099px;top:2292px"></div>
</div>

<div class="abs footer">
  <div class="flogo"><div class="mark"></div>Marlow Haven Partners</div>
  <h3 style="left:371px;top:50px">QUICK LINKS</h3>
  <ul class="links">
    <li>Contact Us</li>
    <li>Learn</li>
    <li>Caregiver Jobs</li>
    <li>Nurse Aide Care</li>
    <li>24-Hour Home Care</li>
    <li>Skilled Nursing</li>
    <li>Lifestyle Aide</li>
    <li>Hospice at Home</li>
    <li>Bathing &amp; Meal Service</li>
  </ul>
  <div class="divider" style="left:539px;top:63px;height:235px"></div>
  <h3 style="left:582px;top:50px">CONTACT INFO</h3>
  <div class="ci" style="top:94px">
    <div class="row"><svg width="12" height="12" viewBox="0 0 24 24"><path fill="#fff" d="M6.6 10.8a15 15 0 0 0 6.6 6.6l2.2-2.2c.3-.3.7-.4 1-.2 1.1.4 2.3.6 3.6.6.6 0 1 .4 1 1V20c0 .6-.4 1-1 1A17 17 0 0 1 3 4c0-.6.4-1 1-1h3.5c.6 0 1 .4 1 1 0 1.2.2 2.4.6 3.6.1.3 0 .7-.2 1z"/></svg><b>Phone</b></div>
    <div style="padding-left:17px">808-555-0173</div>
  </div>
  <div class="ci" style="top:145px">
    <div class="row"><svg width="12" height="10" viewBox="0 0 24 18" style="margin-top:4px"><rect width="24" height="18" rx="2" fill="#fff"/><path d="M1 2l11 8 11-8" stroke="#174a4a" stroke-width="2" fill="none"/></svg><b>Email</b></div>
    <div style="padding-left:17px">info@marlowhaven.example</div>
  </div>
  <div class="ci" style="top:195px">
    <div class="row"><svg width="10" height="13" viewBox="0 0 16 22" style="margin-top:3px"><path fill="#fff" d="M8 0a8 8 0 0 0-8 8c0 6 8 14 8 14s8-8 8-14a8 8 0 0 0-8-8zm0 11a3 3 0 1 1 0-6 3 3 0 0 1 0 6z"/></svg><b>Address:</b></div>
    <div style="padding-left:17px">248 Lanakila Ave, Suite 310,<br>Honolulu, HI 96817</div>
  </div>
  <div class="divider" style="left:818px;top:63px;height:235px"></div>
  <h3 style="left:865px;top:50px">FOLLOW US</h3>
  <div class="soc" style="left:864px"></div>
  <div class="soc" style="left:907px"></div>
  <div class="soc" style="left:951px"></div>
  <div class="soc" style="left:995px"></div>
  <div class="badge" style="left:865px"></div>
  <div class="badge" style="left:953px"></div>
  <div class="rule"></div>
  <div class="copy">© 2024 Marlow Haven Partners. All Rights Reserved.</div>
  <div class="chat"></div>
</div>

</body>
</html>
```